Unternehmensbroschüre / Produktübersicht
Alles super. Die Kommunikation und die Professionalität haben mich überzeugt. Henrike war sehr hilfsbereit und hat mich umfänglich beraten und betreut. Gerne wieder! Vielen Dank. LG Ulf
Zielgruppe
Wir sind Rohmaterial Händler für die Luft- und Raumfahrt Industrie und andere Branchen wie Medizintechnik, Automotive, kommerzieller Maschinenbau etc. und liefern Halbzeuge aus Stahl, Titan, Aluminium, Nickel und Sonderwerkstoffen. Siehe unsere Webseite www.kalvorstahl.de - Unsere Zielgruppe ist nur B2B - unsere Kunden sind Veltrion, Nordavia etc. und deren Zerspaner.
Aufgabenstellung
Wir möchten eine 4-5 seitige Unternehmensbroschüre bzw. Produktübersicht als PDF zum herunterladen für unsere Webseite etc. und gerne auch als gedrucktes Exemplar zum verteilen an Kunden im Außendienst erstellen lassen. Wir machen gerade auch eine neue Webseite. Hier der Link zur neuen Startseite, der neuen Webseite - da seht ihr auch ca. unser Design und so weiter - die Broschüre sollte zu dem Desgin der neuen Webseite passen... also blau und so Weltall Charakter vielleicht:
https://www.entwurfsraum.de/proto/Kq27Tb8xWm41Zr05Ld3Hva/Kalvorstahl?node-id=4102-617&p=f
Und dort soll man die Broschüre auch direkt oben im Header herunterladen können.
Wir haben aktuell eine Produktübersicht über 2 Seiten mit allen Werkstoffen aber ohne Text zu uns und ohne Ansprechpartner und ohne Bilder. Die aktuelle Produktübersicht habe ich unten verlinkt. Die ist nicht wirklich schön und wir möchten daraus 4-5 Seiten machen und noch Bilder hinzufügen etc. und auch unsere Ansprechpartner - dafür habe ich unsere Firmenpräsi nochmal verlinkt, da sieht man auf der letzten Seite die Ansprechpartner, die auch gerne in die Broschüre kommen können.
Ich habe unten auch Bilder von unserer Halle verlinkt aber bitte auch von unserer Seite das Stockfootage von den Produkten nehmen. Wenn das nicht geht, dann eigenes passendes kaufen. Bitte an unseren Produktbildern zu Stahl, Aluminium, Titan etc. orientieren, die auf der neuen oder noch aktuellen Webseite sind. In der Broschüre sollen alle Werkstoffe auftauchen, die in der Produktübersicht sind aber wie oben beschrieben halt auch noch bisschen Text über uns und Bilder usw. damit es schöner und ansprechender für die Kunden ist und nicht nur eine Liste mit Werkstoffen die wir anbieten.
Ich habe von TEXTO BOT mal ein Beispiel anfertigen lassen aber das ist nur ein erster SHOT und..

```html
<!DOCTYPE html>
<html lang="de">
<head>
<meta charset="utf-8">
<title>Kalvorstahl – Broschüre</title>
<link href="https://fonts.googleapis.com/css2?family=Inter:wght@300;400;500;600;700&display=swap" rel="stylesheet">
<style>
:root{
  --board:#a8a8a8;
  --black:#050608;
  --navy:#0a0f1e;
  --navy-2:#141b30;
  --space:#1a2136;
  --teal:#0f3347;
  --blue:#2f6bff;
  --white:#ffffff;
  --muted:#b9c0cf;
  --cell:#c7ced8;
  --cell-text:#1d2433;
  --line:#d9dde6;
}
*{margin:0;padding:0;box-sizing:border-box}
html,body{width:734px;height:1200px;overflow:hidden;background:var(--board)}
body{position:relative;font-family:'Inter',Arial,sans-serif;color:var(--white)}
.page{position:absolute;width:218px;height:309px;overflow:hidden}
.p1{left:135px;top:108px;background:var(--black)}
.p2{left:381px;top:108px;background:var(--navy)}
.p3{left:135px;top:445px;background:var(--navy-2)}
.p4{left:381px;top:445px;background:linear-gradient(180deg,#0d3a52 0%,#0b2536 60%,#0a1526 100%)}
.p5{left:136px;top:783px;background:radial-gradient(ellipse at 40% 30%,#24304e 0%,#151c30 55%,#0d1222 100%)}
.photo{position:absolute}
.brand{position:absolute;font-weight:700;letter-spacing:.6px;color:var(--white);font-size:7px;line-height:1}
.brand small{display:block;font-size:2px;font-weight:700;letter-spacing:.3px;margin-top:1px}

/* cover */
.p1 .brand{left:14px;top:18px}
.cover-title{position:absolute;left:14px;top:51px;font-size:11px;font-weight:700;line-height:13px;letter-spacing:-.3px;width:190px}
.cover-tag{position:absolute;left:14px;top:85px;font-size:7.4px;letter-spacing:1px;font-weight:400}
.cover-rule{position:absolute;left:14px;top:100px;width:33px;height:1px;background:var(--blue)}
.cover-sub{position:absolute;left:14px;top:107px;font-size:4.2px;line-height:6px;color:#d6dae2;width:160px}
.p1 .photo{left:0;top:140px;width:218px;height:169px;background:linear-gradient(170deg,#050608 0%,#0c1a33 30%,#1f4f8c 60%,#3a6fa8 80%,#7c93ad 100%)}

/* about */
.p2 .photo{left:0;top:0;width:218px;height:152px;background:radial-gradient(ellipse at 50% 60%,#3c4a78 0%,#141a2e 45%,#04060c 80%),#04060c}
.h-section{position:absolute;font-weight:600;color:var(--white)}
.about-title{left:13px;top:171px;font-size:8.5px}
.about-text{position:absolute;left:13px;top:185px;width:90px;font-size:3.2px;line-height:5px;color:#d2d7e2}
.about-text p{margin-bottom:3px}
.about-text ul{list-style:none;margin-left:4px}
.about-text li::before{content:"•";color:var(--blue);margin-right:2px}
.branches-title{left:122px;top:183px;font-size:5.5px}
.branches{position:absolute;left:122px;top:196px;list-style:none;font-size:3.3px;font-weight:600}
.branches li{display:flex;align-items:center;height:13.7px}
.branches svg{width:10px;height:10px;margin-right:3px}
.claim{position:absolute;left:13px;top:268px;width:192px;height:28px;border:.5px solid #3a4360;border-radius:3px;background:#111831;padding:4px 7px}
.claim h3{font-size:5.5px;font-weight:500;margin-bottom:4px}
.claim p{font-size:3.2px;line-height:5px;color:#b9c0cf}

/* product pages */
.head-photo{position:absolute;left:0;top:0;width:218px}
.p3 .head-photo{height:53px;background:linear-gradient(90deg,#2a3448 0%,#5a6e8c 40%,#3e5676 70%,#6c7fa0 100%)}
.p4 .head-photo{height:123px;background:linear-gradient(135deg,#6f7b88 0%,#a7b0ba 40%,#8c96a3 65%,#c9a0ae 85%,#9aa3ad 100%)}
.prod-title{position:absolute;left:14px;top:16px;font-size:8.5px;font-weight:700;line-height:9.5px;letter-spacing:-.2px;text-shadow:0 0 4px rgba(0,0,0,.4)}
.prod-sub{position:absolute;left:14px;top:37px;font-size:3.2px;line-height:4.4px;color:#e6e9ef;width:100px}
.side-photos{position:absolute;left:0;top:63px;width:73px}
.side-photos div{height:57px;margin-bottom:1px}
.sp1{background:linear-gradient(180deg,#cfe0f2,#8ea3b8)}
.sp2{background:linear-gradient(180deg,#3e5a7a,#9a8a70)}
.sp3{background:linear-gradient(180deg,#4f6b8c,#c79a5e)}
.sp4{background:linear-gradient(180deg,#6a87a6,#c7ccd2)}
.tables{position:absolute;left:92px;top:62px;width:113px}
.tbl-title{font-size:5px;font-weight:500;letter-spacing:.2px;margin-top:5px;padding-bottom:1px;border-bottom:.5px solid var(--line)}
.tbl-title:first-child{margin-top:0}
.row{display:grid;grid-template-columns:37px 27px 49px;font-size:3px;line-height:3.6px;padding:1.3px 0;border-bottom:.3px solid rgba(255,255,255,.25);color:#dfe3ea}
.row.hd{font-weight:600;color:var(--white);border-bottom:.5px solid var(--line)}

.p4 .col-title{position:absolute;top:139px;font-size:5px;font-weight:500;letter-spacing:.2px}
.alu{position:absolute;left:13px;top:146px;width:75px}
.cell-row{display:grid;grid-template-columns:37px 38px;background:var(--cell);color:var(--cell-text);font-size:3px;line-height:3.6px;padding:1.8px 2px;margin-bottom:.8px}
.cell-row span:last-child{color:#737b8a;font-size:2.7px}
.steel{position:absolute;left:95px;top:146px;width:110px;display:grid;grid-template-columns:54px 54px;column-gap:1.5px;align-items:start}
.steel-col div,.special div{background:var(--cell);color:var(--cell-text);font-size:3px;line-height:3.6px;padding:1.8px 2px;margin-bottom:.8px}
.special-title{left:96px;top:216px}
.special{position:absolute;left:96px;top:223px;width:109px}

/* contacts */
.contact-title{left:15px;top:19px;font-size:8.5px;letter-spacing:-.2px}
.contact-sub{position:absolute;left:15px;top:31px;font-size:3.4px;color:#c9cfdb}
.cards{position:absolute;left:13px;top:54px;display:grid;grid-template-columns:94px 94px;gap:5px 5px}
.card{height:40px;border:.5px solid #6a7392;background:rgba(80,90,120,.35);border-radius:1px;display:flex;padding:3px}
.portrait{width:27px;height:33px;background:linear-gradient(180deg,#6b7486,#2b3242);flex:none}
.card-body{margin-left:4px;font-size:2.9px;line-height:3.9px;color:#d8dce6}
.card-body strong{display:block;font-size:3.8px;color:var(--white);font-weight:700;line-height:4.2px}
.card-body .role{font-size:2.6px;color:#aab1c0;margin-bottom:2.5px;display:block}
.card-body b{color:var(--white)}
.kontakt{position:absolute;left:12px;top:255px}
.kontakt h3{font-size:6px;font-weight:300;letter-spacing:.4px;margin-bottom:4px}
.kontakt p{font-size:3.2px;line-height:5.3px;color:#d2d7e2}
.kontakt p strong{color:var(--white)}
.kontakt svg{width:3.4px;height:3.4px;vertical-align:-.5px;margin-right:1px}
.p5 .brand{left:150px;top:281px}
</style>
</head>
<body>

<section class="page p1">
  <div class="brand">KALVORSTAHL<small>TITAN &amp; METALLHANDELSGESELLSCHAFT</small></div>
  <h1 class="cover-title">High Performance Rohmaterialien für Luft- und Raumfahrt</h1>
  <p class="cover-tag">PRÄZISION. QUALITÄT. VERLÄSSLICHKEIT.</p>
  <div class="cover-rule"></div>
  <p class="cover-sub">Halbzeuge aus Stahl, Titan, Aluminium, Nickel und Sonderwerkstoffen für höchste industrielle Anforderungen</p>
  <div class="photo" role="img" aria-label="Raumstation und Raumfähre im Orbit über der Erde"></div>
</section>

<section class="page p2">
  <div class="photo" role="img" aria-label="Satellit mit Solarpaneelen im Weltall über der Erde"></div>
  <h2 class="h-section about-title">Über uns</h2>
  <div class="about-text">
    <p>KALVORSTAHL ist ein spezialisierter Händler für hochwertige Rohmaterialien mit Fokus auf die Luft- und Raumfahrtindustrie sowie angrenzende High-Tech-Branchen.</p>
    <p>Wir beliefern namhafte Unternehmen wie Veltrion, Nordavia sowie deren Zulieferer und Zerspanungsbetriebe mit präzise gefertigten Halbzeugen aus anspruchsvollen Werkstoffen.</p>
    <p>Unsere Stärke liegt in der Kombination aus:</p>
    <ul><li>tiefem Material-Know-how</li><li>hoher Lieferzuverlässigkeit</li><li>und konsequenter Kundenorientierung</li></ul>
  </div>
  <h3 class="h-section branches-title">Unsere Branchen</h3>
  <ul class="branches">
    <li><svg viewBox="0 0 10 10" fill="none" stroke="#fff" stroke-width=".5"><path d="M2 8 L8 2 M5 2 L8 2 L8 5"/></svg>Luft- und Raumfahrt</li>
    <li><svg viewBox="0 0 10 10" fill="none" stroke="#fff" stroke-width=".5"><circle cx="5" cy="5" r="4"/><path d="M5 3v4M3 5h4"/></svg>Medizintechnik</li>
    <li><svg viewBox="0 0 10 10" fill="none" stroke="#fff" stroke-width=".5"><path d="M1 6h8v1.5H1z M2.5 6l1.5-2h3l1.5 2"/></svg>Automotive</li>
    <li><svg viewBox="0 0 10 10" fill="none" stroke="#fff" stroke-width=".5"><circle cx="4" cy="4" r="2.5"/><circle cx="7" cy="7" r="2"/></svg>Maschinenbau</li>
    <li><svg viewBox="0 0 10 10" fill="none" stroke="#fff" stroke-width=".5"><path d="M1 9V5l3-2v2l3-2v2l2-1v5z"/></svg>Weitere industrielle Anwendungen</li>
  </ul>
  <div class="claim">
    <h3>Unser Anspruch</h3>
    <p>Wir liefern nicht nur Materialien –<br>wir liefern die Grundlage für Innovation, Sicherheit und Präzision.</p>
  </div>
</section>

<section class="page p3">
  <div class="head-photo" role="img" aria-label="Hochregallager mit Metallhalbzeugen"></div>
  <h2 class="prod-title">Produktübersicht -<br>Hochleistungswerkstoffe</h2>
  <p class="prod-sub">Lieferformen: Rundstange, Blech/Platte, Flach, Rohr, Zuschnitt, Profile oder Metallpulver</p>
  <div class="side-photos">
    <div class="sp1" role="img" aria-label="Lagerhalle des Unternehmens von außen"></div>
    <div class="sp2" role="img" aria-label="Gabelstapler mit Rundstangen im Lager"></div>
    <div class="sp3" role="img" aria-label="Regale mit Metallhalbzeugen"></div>
    <div class="sp4" role="img" aria-label="Aluminium-Ronden in der Halle"></div>
  </div>
  <div class="tables">
    <h3 class="tbl-title">TITAN WERKSTOFFE</h3>
    <div class="row hd"><span>Material</span><span>W.-Nr.</span><span>Norm</span></div>
    <div class="row"><span>Titan Grade 1</span><span>3.7024</span><span>WL 3.7024.1 / LN9297</span></div>
    <div class="row"><span>Titan Grade 2</span><span>3.7035</span><span>ASTM B-348 / ASTM B-265</span></div>
    <div class="row"><span>Titan Grade 5</span><span>3.7164</span><span>WL 3.7164 / AMS 4928 / AMS 4911 / MIL-T-9047</span></div>
    <h3 class="tbl-title">STAHL WERKSTOFFE</h3>
    <div class="row hd"><span>Material</span><span>W.-Nr.</span><span>Norm</span></div>
    <div class="row"><span>15-5 PH</span><span>1.4545</span><span>WL 1.4545.4 / AMS 5659</span></div>
    <div class="row"><span>17-4 PH</span><span>1.4548</span><span>WL 1.4548.4 / AMS 5643</span></div>
    <div class="row"><span>PH 13-8 Mo</span><span>1.4534</span><span>WL 1.4534.4 / AMS 5864</span></div>
    <div class="row"><span>15CDV6</span><span>1.7734</span><span>WL 1.7734 / AIR9160C</span></div>
    <div class="row"><span>Weitere Werkstoffe</span><span>–</span><span>Weitere Luftfahrtstähle auf Anfrage</span></div>
    <h3 class="tbl-title">ALUMINIUM WERKSTOFFE</h3>
    <div class="row hd"><span>Material</span><span>W.-Nr.</span><span>Norm</span></div>
    <div class="row"><span>EN AW-2024</span><span>3.1354</span><span>WL 3.1354 / 3.1364</span></div>
    <div class="row"><span>EN AW-6061</span><span>3.3214</span><span>WL 3.3214</span></div>
    <div class="row"><span>EN AW-7075/7175</span><span>3.4364</span><span>WL 3.4364</span></div>
    <div class="row"><span>EN AW-7050</span><span>3.4144</span><span>WL 3.4144</span></div>
    <h3 class="tbl-title">NICKEL- UND SONDERWERKSTOFFE</h3>
    <div class="row hd"><span>Material</span><span>W.-Nr.</span><span>Norm</span></div>
    <div class="row"><span>Ferrinar 36</span><span>1.3912</span><span>ASTM-F1684 / UNS K93603</span></div>
    <div class="row"><span>Ferrinar 42 – Alloy 42</span><span>1.3917</span><span>ASTM-F30 / UNS K94100</span></div>
    <div class="row"><span>Nickelor 625</span><span>2.4856</span><span>UNS N06625 / ASTM-B446</span></div>
    <div class="row"><span>Nickelor 718</span><span>2.4668</span><span>UNS N07718 / AMS 5662</span></div>
    <div class="row"><span>Alloy K – Koveral</span><span>1.3980 / 1.3981</span><span>ASTM-F15 / UNS K94610</span></div>
    <h3 class="tbl-title">US-AMERIKANISCHE WERKSTOFFE</h3>
    <div class="row hd"><span>Material</span><span>W.-Nr.</span><span>Norm</span></div>
    <div class="row"><span>Maraging 250</span><span>–</span><span>AMS 6512</span></div>
    <div class="row"><span>Alloy 4130</span><span>–</span><span>AMS 6348</span></div>
    <div class="row"><span>Alloy 440C / A-286</span><span>–</span><span>AMS 5630 / AMS 5731 / 5732 / 5737</span></div>
  </div>
</section>

<section class="page p4">
  <div class="head-photo" role="img" aria-label="Sägezentrum in der Halle mit gestapelten Metallronden auf Paletten"></div>
  <h2 class="prod-title">Produktübersicht -<br>Standardwerkstoffe</h2>
  <p class="prod-sub">Lieferformen: Rundstange, Blech/Platte, Flach, Rohr, Zuschnitt, Profile oder Metallpulver</p>
  <h3 class="col-title" style="left:13px">ALUMINIUM WERKSTOFFE</h3>
  <h3 class="col-title" style="left:95px">STAHL WERKSTOFFE</h3>
  <div class="alu">
    <div class="cell-row"><span>EN AW-1050A</span><span>W.-Nr. 3.0255</span></div>
    <div class="cell-row"><span>EN AW-6012</span><span>W.-Nr. 3.0615</span></div>
    <div class="cell-row"><span>EN AW-2007</span><span>W.-Nr. 3.1645</span></div>
    <div class="cell-row"><span>EN AW-6082</span><span>W.-Nr. 3.2315</span></div>
    <div class="cell-row"><span>EN AW-2024</span><span>W.-Nr. 3.1354</span></div>
    <div class="cell-row"><span>EN AW-7022</span><span>W.-Nr. 3.4345</span></div>
    <div class="cell-row"><span>EN AW-5754</span><span>W.-Nr. 3.3535</span></div>
    <div class="cell-row"><span>EN AW-1350A</span><span>W.-Nr. 3.0257</span></div>
    <div class="cell-row"><span>EN AW-6061</span><span>W.-Nr. 3.3214</span></div>
    <div class="cell-row"><span>EN AW-2017A</span><span>W.-Nr. 3.1325</span></div>
    <div class="cell-row"><span>EN AW-7020</span><span>W.-Nr. 3.4335</span></div>
    <div class="cell-row"><span>EN AW-7050 / 7075 / 7175</span><span>W.-Nr. 3.4144 / 3.4364</span></div>
    <div class="cell-row"><span>EN AW-1080</span><span>W.-Nr. 3.0255</span></div>
    <div class="cell-row"><span>EN AW-6060</span><span>W.-Nr. 3.3206</span></div>
    <div class="cell-row"><span>EN AW-2011</span><span>W.-Nr. 3.1655</span></div>
    <div class="cell-row"><span>EN AW-6101</span><span>W.-Nr. 3.3207</span></div>
    <div class="cell-row"><span>EN AW-5019</span><span>W.-Nr. 3.3555</span></div>
  </div>
  <div class="steel">
    <div class="steel-col">
      <div>Automatenstahl</div><div>Warmfester Stahl</div><div>Nitrierstahl</div><div>Einsatzstahl</div>
      <div>Druckbehälterstahl</div><div>Wälzlagerstahl</div><div>RSH-Stahl</div><div>Vergütungsstahl</div>
    </div>
    <div class="steel-col">
      <div>Präzisionsflachstahl</div><div>Schnellarbeitsstahl</div><div>Kaltarbeitsstahl</div><div>Warmarbeitsstahl</div>
      <div>Unlegierter Werkzeugstahl</div><div>und weitere Stahl Werkstoffe auf Anfrage</div>
    </div>
  </div>
  <h3 class="col-title special-title" style="top:216px">SONDERWERKSTOFFE</h3>
  <div class="special">
    <div>Kupfer, niedriglegierte Kupferlegierungen &amp; Kupfer-Nickel</div>
    <div>Messing &amp; Sondermessing</div>
    <div>Guss-Zinnbronze &amp; Rotguss</div>
    <div>Zinnbronze, Aluminiumbronze &amp; Bleibronze</div>
    <div>Gusseisen</div>
    <div>Kunststoffe</div>
    <div>und weitere Sonderwerkstoffe auf Anfrage</div>
  </div>
</section>

<section class="page p5">
  <h2 class="h-section contact-title">Ihr direkter Ansprechpartner</h2>
  <p class="contact-sub">Unser Team steht Ihnen jederzeit kompetent und persönlich zur Verfügung.</p>
  <div class="cards">
    <div class="card"><div class="portrait" role="img" aria-label="Porträtfoto Geschäftsführer"></div><div class="card-body"><strong>Gerhard T. Wendland</strong><span class="role">Geschäftsführer, Inhaber</span><b>E.</b> g.wendland@kalvorstahl.de<br><b>T.</b> +49 61 72 481 55- 13<br><b>F.</b> +49 61 72 481 55- 20</div></div>
    <div class="card"><div class="portrait" role="img" aria-label="Porträtfoto Geschäftsführer"></div><div class="card-body"><strong>Jonas R. Wendland</strong><span class="role">Geschäftsführer, Inhaber</span><b>E.</b> j.wendland@kalvorstahl.de<br><b>T.</b> +49 61 72 481 55- 15<br><b>F.</b> +49 61 72 481 55- 20</div></div>
    <div class="card"><div class="portrait" role="img" aria-label="Porträtfoto kaufmännische Leiterin"></div><div class="card-body"><strong>ppa. Petra Wendland</strong><span class="role">Kaufmännische Leiterin / QM</span><b>E.</b> p.wendland@kalvorstahl.de<br><b>T.</b> +49 61 72 481 55- 17<br><b>F.</b> +49 61 72 481 55- 20</div></div>
    <div class="card"><div class="portrait" role="img" aria-label="Porträtfoto technischer Leiter"></div><div class="card-body"><strong>ppa. Tobias Reinhalt</strong><span class="role">Technischer Leiter</span><b>E.</b> t.reinhalt@kalvorstahl.de<br><b>T.</b> +49 61 72 481 55- 18<br><b>F.</b> +49 61 72 481 55- 20</div></div>
    <div class="card"><div class="portrait" role="img" aria-label="Porträtfoto Verkaufsleiter"></div><div class="card-body"><strong>ppa. Dmitri Solanek</strong><span class="role">Verkaufsleiter</span><b>E.</b> d.solanek@kalvorstahl.de<br><b>T.</b> +49 61 72 481 55- 14<br><b>F.</b> +49 61 72 481 55- 20</div></div>
    <div class="card"><div class="portrait" role="img" aria-label="Porträtfoto Innendienstleiterin"></div><div class="card-body"><strong>ppa. Marie Feldhaus</strong><span class="role">Innendienstleiterin</span><b>E.</b> m.feldhaus@kalvorstahl.de<br><b>T.</b> +49 61 72 481 55- 19<br><b>F.</b> +49 61 72 481 55- 20</div></div>
  </div>
  <div class="kontakt">
    <h3>Kontakt</h3>
    <p><strong>KALVORSTAHL</strong><br>
    <svg viewBox="0 0 4 4"><circle cx="2" cy="2" r="1.7" fill="none" stroke="#4a7bff" stroke-width=".4"/></svg>www.kalvorstahl.de<br>
    <svg viewBox="0 0 4 4"><rect x=".3" y=".8" width="3.4" height="2.4" fill="none" stroke="#4a7bff" stroke-width=".4"/><path d="M.3.8L2 2.2 3.7.8" fill="none" stroke="#4a7bff" stroke-width=".4"/></svg>info@kalvorstahl.de<br>
    <svg viewBox="0 0 4 4"><path d="M1 .5l.8 1-.5.6a2.5 2.5 0 0 0 .8.8l.6-.5 1 .8-.6.8C1.8 3.8.2 2.2.4 1z" fill="none" stroke="#4a7bff" stroke-width=".35"/></svg>+49 (0) XXX XXXXXXX</p>
  </div>
  <div class="brand">KALVORSTAHL<small>TITAN &amp; METALLHANDELSGESELLSCHAFT</small></div>
</section>

</body>
</html>
```